CyberSecurity Company Website Design

DO NOT CONTACT US OUTSIDE OF PIXELBAZAAR.COM!

A professional 5 page website design for a cyber security and risk management company. We want to portray a serious and professional approach to online security and risk management for businesses. We want the website to be easy to navigate but with a modern style.

The website design pages my partners have reviewed and wish to emulate (without copying, of course ) are:
wrenforge.com, larkhollow.com and brunel.com, Gavromill.com

The attached Zip file contains a very basic outline of the format we are looking for. We want a nice, modern design that reflects cyber security, securing networks, and risk management for business.

Target Market(s)

Large corporations with CyberSecurity Needs

Number of Pages Required

5+ page

Colors
ec1f27
ffffff
0293ce

Requirements
Must have
• The 5 pages we need designed are;
• Home page, Services, About Us, Careers and Contact.

```html
<!DOCTYPE html>
<html lang="en">
<head>
<meta charset="utf-8">
<title>Veridane CyberTech – Website Pages</title>
<link href="https://fonts.googleapis.com/css2?family=Roboto:wght@400;500;700;900&family=Open+Sans:wght@400;600&display=swap" rel="stylesheet">
<style>
:root{
  --board:#5ec4f6;
  --red:#ec1f27;
  --blue:#0293ce;
  --heading:#1b7cc4;
  --ink:#222;
  --muted:#777;
  --footer:#0b0b0b;
  --white:#fff;
  --hero-dark:#2a2d33;
  --hero-mid:#5b6068;
  --hero-light:#a3a7ad;
  --hero-tint:#3c5a72;
}
*{box-sizing:border-box;margin:0;padding:0}
html,body{width:1200px;height:4534px;overflow:hidden}
body{background:var(--board);position:relative;font-family:'Open Sans',Arial,sans-serif;color:var(--ink)}
.page{position:absolute;left:106px;width:988px;background:var(--white);overflow:hidden;box-shadow:0 2px 10px rgba(0,0,0,.15)}
.hero{position:relative;width:100%;color:var(--white);text-align:center}
.hero-photo{position:absolute;inset:0;
  background:
    radial-gradient(ellipse 32% 55% at 76% 52%,rgba(210,215,222,.55),transparent 70%),
    radial-gradient(ellipse 40% 60% at 28% 30%,rgba(150,155,162,.45),transparent 70%),
    radial-gradient(ellipse 50% 40% at 20% 95%,rgba(60,90,114,.55),transparent 75%),
    linear-gradient(115deg,var(--hero-dark) 0%,var(--hero-mid) 38%,var(--hero-light) 60%,var(--hero-mid) 80%,var(--hero-dark) 100%)}
.hero-photo::after{content:"";position:absolute;inset:0;background:linear-gradient(180deg,rgba(0,0,0,.25),rgba(0,0,0,.1) 40%,rgba(0,0,0,.35))}
.topbar{position:absolute;top:0;left:0;right:0;height:100px;display:flex;align-items:center;justify-content:space-between;padding:0 60px 0 88px;z-index:2}
.brand-small{display:flex;align-items:center;gap:8px;font-family:'Roboto',sans-serif;font-weight:700;font-size:22px;color:var(--white)}
.brand-small .mark{width:14px;height:14px;background:var(--red)}
.nav{display:flex;gap:22px;align-items:center;font-family:'Roboto',sans-serif;font-weight:500;font-size:13px;letter-spacing:.3px}
.nav a{color:var(--white);text-decoration:none}
.nav a.active{color:var(--red)}
.hero-inner{position:relative;z-index:1}
.brand-large{display:inline-flex;align-items:center;gap:14px;font-family:'Roboto',sans-serif;font-weight:700;font-size:66px;color:var(--white)}
.brand-large .mark{width:40px;height:40px;background:var(--red)}
.slogan{font-family:'Roboto',sans-serif;font-weight:900;font-size:60px;word-spacing:22px;letter-spacing:.5px}
.hero-title{font-family:'Roboto',sans-serif;font-weight:900;font-size:56px;line-height:1.13}
.section{text-align:center}
.section h2{font-family:'Roboto',sans-serif;font-weight:700;font-size:28px;color:var(--heading)}
.lead{font-size:13px;color:var(--muted);line-height:1.75}
.footer{position:relative;background:var(--footer);color:var(--white);text-align:center;font-size:11.5px}
.footer .office{font-family:'Roboto',sans-serif;font-weight:700;font-size:17px;padding-top:30px}
.footer .area{font-size:12px;margin-top:4px}
.contacts{display:flex;justify-content:center;align-items:center;gap:12px;margin-top:14px}
.contacts span{display:inline-flex;align-items:center;gap:6px}
.contacts i{display:inline-block;width:1px;height:12px;background:#777}
.copy{margin-top:12px}
.social{position:absolute;right:86px;top:-18px;display:flex;gap:10px;z-index:3}
.social span{width:34px;height:34px;border-radius:50%;background:var(--white);border:1px solid #888}
.team{display:flex;justify-content:center;gap:42px;margin-top:52px}
.member{width:248px}
.member .photo{width:248px;height:248px;border-radius:50%;border:5px solid #e5e5e5;background:linear-gradient(160deg,#8a7a70,#3c3230)}
.member h3{font-family:'Roboto',sans-serif;font-weight:700;font-size:18px;margin-top:30px}
.member p{font-size:13px;color:var(--blue);margin-top:10px}
.cards{display:flex;justify-content:center;gap:15px;margin-top:58px}
.card{position:relative;width:265px;height:262px;border:2px solid #d6d6d6;border-radius:14px;padding:22px 18px 0}
.card .avatar{width:100px;height:100px;border-radius:50%;margin:0 auto;border:3px solid #e5e5e5;background:linear-gradient(160deg,#7b8590,#2f3640)}
.card h3{font-family:'Roboto',sans-serif;font-weight:700;font-size:18px;margin:12px 0 8px}
.card p{font-size:10.5px;color:#555;line-height:1.55}
.card .badge{position:absolute;left:50%;bottom:-20px;transform:translateX(-50%);width:40px;height:40px;border-radius:50%}
</style>
</head>
<body>

<section class="page" style="top:106px;height:1082px">
  <header class="hero" style="height:550px">
    <div class="hero-photo" role="img" aria-label="Photo of hands typing on a laptop keyboard under a glowing circular network security overlay"></div>
    <div class="topbar">
      <div class="brand-small"><span class="mark"></span>Veridane</div>
      <nav class="nav"><a class="active">HOME</a><a>SERVICES</a><a>ABOUT US</a><a>CAREERS</a><a>CONTACT</a>
        <svg width="13" height="13" viewBox="0 0 13 13"><circle cx="5.5" cy="5.5" r="4" fill="none" stroke="#fff" stroke-width="1.8"/><line x1="8.5" y1="8.5" x2="12" y2="12" stroke="#fff" stroke-width="1.8"/></svg></nav>
    </div>
    <div class="hero-inner" style="padding-top:150px">
      <div class="brand-large"><span class="mark"></span>Veridane</div>
      <div class="slogan" style="margin-top:70px">SAFE SAFER VERIDANE</div>
    </div>
  </header>
  <div class="section" style="height:366px;padding-top:56px">
    <h2>WELCOME TO VERIDANE CYBERTECH (VCT)</h2>
    <p class="lead" style="margin-top:26px">We provide advanced security engineering and cybersecurity architecture solutions for the<br>commercial sector and federal government.</p>
    <p class="lead" style="margin-top:18px">Our security experts create customized IT solutions for private organizations that meet compliance<br>requirements as well required federal and commercial qualifications.</p>
    <p class="lead" style="margin-top:18px">- It's all about YOU, our customer, your needs and your safety.</p>
  </div>
  <footer class="footer" style="height:166px">
    <div class="social"><span></span><span></span><span></span></div>
    <div class="office">Veridane Corporate Office</div>
    <div class="area">Harbor Plaza</div>
    <div class="contacts"><span>&#9742; 1 555 010 0100</span><i></i><span>&#9112; 1 555 010 0199</span><i></i><span>&#9993; info@veridane.com</span></div>
    <div class="copy">Copyrights © 2018, Veridane. All rights reserved.</div>
  </footer>
</section>

<section class="page" style="top:1300px;height:795px">
  <header class="hero" style="height:626px">
    <div class="hero-photo" role="img" aria-label="Photo of hands typing on a laptop keyboard under a glowing circular network security overlay"></div>
    <div class="topbar">
      <div class="brand-small"><span class="mark"></span>Veridane</div>
      <nav class="nav"><a>HOME</a><a class="active">SERVICES</a><a>ABOUT US</a><a>CAREERS</a><a>CONTACT</a>
        <svg width="13" height="13" viewBox="0 0 13 13"><circle cx="5.5" cy="5.5" r="4" fill="none" stroke="#fff" stroke-width="1.8"/><line x1="8.5" y1="8.5" x2="12" y2="12" stroke="#fff" stroke-width="1.8"/></svg></nav>
    </div>
    <div class="hero-inner" style="padding-top:150px">
      <div class="brand-large"><span class="mark"></span>Veridane</div>
      <div class="slogan" style="margin-top:70px">SAFE SAFER VERIDANE</div>
      <div style="font-family:'Open Sans',sans-serif;font-weight:600;font-size:22px;margin-top:4px">Veridane CyberTech (Vct)</div>
      <div style="font-family:'Open Sans',sans-serif;font-weight:600;font-size:31px;margin-top:6px">Products &amp; Service Listings Coming Soon</div>
    </div>
  </header>
  <footer class="footer" style="height:169px">
    <div class="social"><span></span><span></span><span></span></div>
    <div class="office">Veridane Corporate Office</div>
    <div class="area">Harbor Plaza</div>
    <div class="contacts"><span>&#9742; 1 555 010 0100</span><i></i><span>&#9112; 1 555 010 0199</span><i></i><span>&#9993; info@veridane.com</span></div>
    <div class="copy">Copyrights © 2018, Veridane. All rights reserved.</div>
  </footer>
</section>

<section class="page" style="top:2198px;height:1082px">
  <header class="hero" style="height:350px">
    <div class="hero-photo" role="img" aria-label="Photo of hands typing on a laptop keyboard under a glowing circular network security overlay"></div>
    <div class="topbar">
      <div class="brand-small"><span class="mark"></span>Veridane</div>
      <nav class="nav"><a>HOME</a><a>SERVICES</a><a class="active">ABOUT US</a><a>CAREERS</a><a>CONTACT</a>
        <svg width="13" height="13" viewBox="0 0 13 13"><circle cx="5.5" cy="5.5" r="4" fill="none" stroke="#fff" stroke-width="1.8"/><line x1="8.5" y1="8.5" x2="12" y2="12" stroke="#fff" stroke-width="1.8"/></svg></nav>
    </div>
    <div class="hero-inner" style="padding-top:118px">
      <h1 class="hero-title">AMAZING TEAM<br>AT VERIDANE</h1>
    </div>
  </header>
  <div class="section" style="height:566px;padding-top:62px">
    <h2>MEET OUR PARTNERS</h2>
    <p class="lead" style="margin-top:8px">Veridane CyberTech (Vct)</p>
    <div class="team">
      <div class="member"><div class="photo" role="img" aria-label="Portrait photo of the CEO"></div><h3>Mark Halvorsen</h3><p>CEO</p></div>
      <div class="member"><div class="photo" role="img" aria-label="Portrait photo of the VP of Business Development"></div><h3>Lena Dorsey</h3><p>VP Business Development</p></div>
      <div class="member"><div class="photo" role="img" aria-label="Portrait photo of the CTO"></div><h3>Rafael Ocampo</h3><p>CTO</p></div>
    </div>
  </div>
  <footer class="footer" style="height:166px">
    <div class="social"><span></span><span></span><span></span></div>
    <div class="office">Veridane Corporate Office</div>
    <div class="area">Harbor Plaza</div>
    <div class="contacts"><span>&#9742; 1 555 010 0100</span><i></i><span>&#9112; 1 555 010 0199</span><i></i><span>&#9993; info@veridane.com</span></div>
    <div class="copy">Copyrights © 2018, Veridane. All rights reserved.</div>
  </footer>
</section>

<section class="page" style="top:3395px;height:1037px">
  <header class="hero" style="height:354px">
    <div class="hero-photo" role="img" aria-label="Photo of hands typing on a laptop keyboard under a glowing circular network security overlay"></div>
    <div class="topbar">
      <div class="brand-small"><span class="mark"></span>Veridane</div>
      <nav class="nav"><a>HOME</a><a>SERVICES</a><a>ABOUT US</a><a class="active">CAREERS</a><a>CONTACT</a>
        <svg width="13" height="13" viewBox="0 0 13 13"><circle cx="5.5" cy="5.5" r="4" fill="none" stroke="#fff" stroke-width="1.8"/><line x1="8.5" y1="8.5" x2="12" y2="12" stroke="#fff" stroke-width="1.8"/></svg></nav>
    </div>
    <div class="hero-inner" style="padding-top:130px">
      <h1 class="hero-title" style="font-size:50px">AWESOME PEOPLE TALK<br>ABOUT VERIDANE CYBERTECH</h1>
    </div>
  </header>
  <div class="section" style="height:520px;padding-top:58px">
    <h2>OUR CUSTOMERS ARE OUR HEROES!</h2>
    <div class="cards">
      <div class="card"><div class="avatar" role="img" aria-label="Customer portrait photo"></div><h3>Owen Pratt</h3><p>Veridane - Love coming your way! Best cybersecurity group we have ever used, prompt and responsive 7 days a week</p><span class="badge" style="background:#3b5998"></span></div>
      <div class="card"><p>No one takes care of our cybersecurity against global threats like Rafael &amp; the Veridane Team</p><div class="avatar" role="img" aria-label="Customer portrait photo" style="margin-top:12px"></div><h3>Gavin Ellery</h3><span class="badge" style="background:#0e76a8"></span></div>
      <div class="card"><div class="avatar" role="img" aria-label="Customer portrait sketch"></div><h3>Peter Lindqvist</h3><p>I can sleep at night, and so can my executive team, thanks to Veridane. They are worth their weight in gold!</p><span class="badge" style="background:#1da1f2"></span></div>
    </div>
  </div>
  <footer class="footer" style="height:163px">
    <div class="social"><span></span><span></span><span></span></div>
    <div class="office">Veridane Corporate Office</div>
    <div class="area">Harbor Plaza</div>
    <div class="contacts"><span>&#9742; 1 555 010 0100</span><i></i><span>&#9112; 1 555 010 0199</span><i></i><span>&#9993; info@veridane.com</span></div>
    <div class="copy">Copyrights © 2018, Veridane. All rights reserved.</div>
  </footer>
</section>

</body>
</html>
```